Criação de Papelaria Profissional para Construção & Engenharia
A empresa queria:
" Empresa de 28 anos, muito centrada no nome FALUCENA que é o sobrenome do dono da empresa e maior diferencial no mercado, a experiência! A empresa preza pela qualidade no atendimento ao cliente, sendo que o ponto forte é estar junto ao cliente em todas as etapas do projeto, principalmente durante a obra "

```html
<!DOCTYPE html>
<html lang="pt-BR">
<head>
<meta charset="UTF-8">
<title>FALUCENA – Papelaria</title>
<link href="https://fonts.googleapis.com/css2?family=Montserrat:wght@400;500&display=swap" rel="stylesheet">
<style>
  :root{
    --stage:#d6d6d6;
    --paper:#ffffff;
    --red:#c4161c;
    --red-dark:#9e1015;
    --grey:#b9b9b9;
    --ink:#3a3a3a;
    --tint:#f1f1f1;
  }
  html,body{margin:0;padding:0;overflow:hidden;}
  body{
    width:1200px;height:1200px;background:var(--stage);
    font-family:"Montserrat",Arial,sans-serif;color:var(--ink);
    position:relative;
  }
  .sheet{
    position:absolute;top:250px;width:460px;height:650px;
    background:var(--paper);box-shadow:0 6px 18px rgba(0,0,0,.18);
    overflow:hidden;
  }
  .envelope{left:90px;}
  .letterhead{left:650px;}
  .envelope-flap{position:absolute;top:0;left:0;width:100%;height:60px;}
  .brand{
    position:absolute;left:0;right:0;display:flex;align-items:center;justify-content:center;gap:12px;
  }
  .brand-dot{width:22px;height:22px;border-radius:50%;background:var(--ink);}
  .brand-name{font-weight:400;font-size:34px;letter-spacing:4px;color:var(--ink);line-height:1;}
  .brand-sub{position:absolute;font-size:7px;letter-spacing:1px;color:var(--ink);}
  .envelope .brand{top:130px;}
  .envelope .brand-sub{top:168px;left:318px;}
  .letterhead .brand{top:540px;}
  .letterhead .brand-sub{top:578px;left:318px;}
  .skyline-area{
    position:absolute;left:20px;right:20px;height:220px;
    background:linear-gradient(180deg,rgba(241,241,241,0) 0%,var(--tint) 100%);
  }
  .envelope .skyline-area{top:205px;}
  .letterhead .skyline-area{top:80px;}
  .contacts{position:absolute;left:26px;top:440px;margin:0;padding:0;list-style:none;font-size:8px;line-height:1;}
  .contacts li{display:flex;align-items:center;gap:6px;margin-bottom:5px;}
  .contact-icon{width:11px;height:11px;border-radius:50%;background:var(--red);flex:none;display:flex;align-items:center;justify-content:center;}
  .contact-icon svg{width:7px;height:7px;}
  .contact-indent{padding-left:17px;}
  .base-band{position:absolute;left:0;bottom:0;width:100%;height:14px;display:flex;}
  .base-band .band-red{width:42%;background:var(--red);}
  .base-band .band-grey{flex:1;background:var(--grey);}
</style>
</head>
<body>

<section class="sheet envelope" aria-label="Envelope">
  <svg class="envelope-flap" viewBox="0 0 460 60" preserveAspectRatio="none">
    <path d="M0 0H460V60H0Z" fill="var(--red)"/>
    <path d="M0 52H460V60H0Z" fill="var(--red-dark)"/>
  </svg>

  <div class="brand"><span class="brand-dot"></span><span class="brand-name">FALUCENA</span></div>
  <span class="brand-sub">obras</span>

  <div class="skyline-area" role="img" aria-label="Ilustração em linha de prédios da cidade"></div>

  <ul class="contacts">
    <li><span class="contact-icon"><svg viewBox="0 0 10 10"><path d="M2 1l2 0 1 2-1 1c.5 1 1 1.5 2 2l1-1 2 1v2c-4 0-7-3-7-7z" fill="#fff"/></svg></span>(11) 4000-2800</li>
    <li><span class="contact-icon"><svg viewBox="0 0 10 10"><rect x="1" y="2.5" width="8" height="5" fill="#fff"/></svg></span>contato@falucena.com.br</li>
    <li><span class="contact-icon"><svg viewBox="0 0 10 10"><circle cx="5" cy="5" r="3.5" fill="none" stroke="#fff"/></svg></span>www.falucena.com.br</li>
    <li><span class="contact-icon"><svg viewBox="0 0 10 10"><path d="M5 1a3 3 0 0 1 3 3c0 2-3 5-3 5S2 6 2 4a3 3 0 0 1 3-3z" fill="#fff"/></svg></span>Rua das Pedras, 28</li>
    <li class="contact-indent">Centro, Cidade - UF CEP 00000-000</li>
  </ul>

  <div class="base-band"><span class="band-red"></span><span class="band-grey"></span></div>
</section>

<section class="sheet letterhead" aria-label="Papel timbrado">
  <div class="skyline-area" role="img" aria-label="Ilustração em linha de prédios da cidade"></div>

  <div class="brand"><span class="brand-dot"></span><span class="brand-name">FALUCENA</span></div>
  <span class="brand-sub">obras</span>

  <div class="base-band"><span class="band-red"></span><span class="band-grey"></span></div>
</section>

</body>
</html>
```